Infographic for Labor Trends - Supply Chain Theme

Looking to polish this slide up to look professional enough to share with the Board of Directors. The focus is Supply Chain Labor (Warehousing and transportation) Need to have a theme around Supply Chain workforce. Needs to be formatted for wide screen PowerPoint

```html
<!DOCTYPE html>
<html lang="en">
<head>
<meta charset="utf-8">
<title>Supply Chain Job Market Remains Tight</title>
<link href="https://fonts.googleapis.com/css2?family=Roboto:wght@400;500;700;900&display=swap" rel="stylesheet">
<style>
  :root {
    --navy: #1b3a5c;
    --ink: #1f2d3d;
    --panel: #bcd8f4;
    --card-bg: #ffffff;
    --muted: #8a94a3;
    --rule: #d7dde4;
    --section: #b5306a;
    --pink: #d94fa4;
    --green: #2f9e4f;
    --orange: #e0a03a;
    --blue: #2c63c9;
    --grid: #e3e7ee;
  }
  * { box-sizing: border-box; margin: 0; padding: 0; }
  html, body { width: 1200px; height: 675px; overflow: hidden; background: #fff; }
  body { font-family: "Roboto", Arial, sans-serif; color: var(--ink); }
  .slide { position: relative; width: 1200px; height: 675px; background: #fff; overflow: hidden; }
  .side-panel {
    position: absolute; left: 0; top: 0; width: 562px; height: 668px;
    background: var(--panel); border-radius: 0 22px 22px 0;
  }
  .slide-title {
    position: absolute; left: 0; top: 10px; width: 1200px; text-align: center;
    font-size: 60px; font-weight: 700; color: var(--navy); letter-spacing: -0.3px;
    white-space: nowrap;
  }
  .key-points {
    position: absolute; left: 40px; top: 93px; width: 482px; list-style: none;
  }
  .key-points li {
    position: relative; padding-left: 24px;
    font-size: 17px; font-weight: 700; line-height: 31.5px; color: var(--navy);
    letter-spacing: 0.3px; text-align: justify;
  }
  .key-points li svg { position: absolute; left: 6px; top: 9px; }
  .sector-table {
    position: absolute; left: 96px; top: 395px; width: 367px; height: 232px;
    background: #fff; box-shadow: 0 0 14px 6px rgba(255,255,255,0.9);
    padding: 5px 12px 0; overflow: hidden;
  }
  .sector-table h3 { text-align: center; font-size: 12.5px; font-weight: 700; color: #111; line-height: 14px; }
  .sector-table .table-sub { text-align: center; font-size: 8.5px; font-weight: 700; color: #333; line-height: 11px; margin-bottom: 2px; }
  .sector-table table { width: 100%; border-collapse: collapse; font-size: 7.8px; color: #222; }
  .sector-table th { font-weight: 400; color: #3c6fb0; font-size: 6.5px; text-align: left; padding: 0 2px; height: 10px; line-height: 9px; border-bottom: 1px solid var(--rule); }
  .sector-table td { padding: 0 2px; height: 10.5px; line-height: 10px; border-bottom: 1px solid #edf0f3; }
  .sector-table tr.group td { color: var(--section); height: 14px; padding-top: 4px; }
  .sector-table tr:nth-child(even):not(.group) td { background: #f3f4f6; }
  .card {
    position: absolute; background: var(--card-bg); border-radius: 22px;
    box-shadow: 0 6px 18px rgba(60,80,110,0.18); overflow: hidden;
  }
  .card svg { display: block; }
  .card-postings { left: 680px; top: 96px; width: 387px; height: 237px; }
  .card-incentives { left: 693px; top: 407px; width: 374px; height: 240px; }
  .postings-note {
    position: absolute; left: 645px; top: 346px; width: 505px;
    font-size: 8.6px; font-weight: 700; color: var(--navy); line-height: 17px; text-align: center;
  }
</style>
</head>
<body>
<div class="slide">
  <div class="side-panel"></div>
  <h1 class="slide-title">Supply Chain Job Market Remains Tight</h1>

  <ul class="key-points">
    <li><svg width="12" height="12" viewBox="0 0 13 13"><path d="M1.5 7 L5 10.5 L11.5 2" fill="none" stroke="var(--navy)" stroke-width="1.6"/></svg>We continue to see pressure and struggle to attract the talent needed to meet staffing demands in multiple market</li>
    <li><svg width="12" height="12" viewBox="0 0 13 13"><path d="M1.5 7 L5 10.5 L11.5 2" fill="none" stroke="var(--navy)" stroke-width="1.6"/></svg>Wage inflation in the industry continues and is amplified lack of talent to cover demand for the holiday season cycle</li>
    <li><svg width="12" height="12" viewBox="0 0 13 13"><path d="M1.5 7 L5 10.5 L11.5 2" fill="none" stroke="var(--navy)" stroke-width="1.6"/></svg>We expect demand to remain extremely high through 2022 period due to the amount of backlog freight at the ports and missed Holiday placement of goods</li>
  </ul>

  <div class="sector-table">
    <h3>Some sectors are booming while others lag</h3>
    <p class="table-sub">% change in US job postings, seasonally adjusted, Oct 8 2021</p>
    <table>
      <tr><th>Sectors</th><th>% change since 2/1/20</th><th>% pt. change vs 4 weeks ago</th></tr>
      <tr class="group"><td colspan="3">Better than economy average</td></tr>
      <tr><td>Human Resources</td><td>92.9%</td><td>9.0%</td></tr>
      <tr><td>Production &amp; Manufacturing</td><td>89.9%</td><td>4.1%</td></tr>
      <tr><td>Loading &amp; Stocking</td><td>89.4%</td><td>6.2%</td></tr>
      <tr><td>Pharmacy</td><td>89.0%</td><td>7.5%</td></tr>
      <tr class="group"><td colspan="3">Similar to economy average</td></tr>
      <tr><td>Driving</td><td>51.4%</td><td>7.0%</td></tr>
      <tr><td>Childcare</td><td>50.6%</td><td>6.0%</td></tr>
      <tr><td>Arts &amp; Entertainment</td><td>44.4%</td><td>2.8%</td></tr>
      <tr><td>Food Preparation &amp; Service</td><td>38.7%</td><td>0.7%</td></tr>
      <tr class="group"><td colspan="3">Worse than economy average</td></tr>
      <tr><td>Sales</td><td>20.0%</td><td>1.6%</td></tr>
      <tr><td>Hospitality &amp; Tourism</td><td>18.6%</td><td>2.1%</td></tr>
      <tr><td>Sports</td><td>13.2%</td><td>2.4%</td></tr>
      <tr><td>Beauty &amp; Wellness</td><td>-3.8%</td><td>-3.5%</td></tr>
    </table>
  </div>

  <div class="card card-postings">
    <svg width="387" height="237" viewBox="0 0 354 240" preserveAspectRatio="none" font-family="Roboto, Arial, sans-serif">
      <text x="177" y="22" text-anchor="middle" font-size="10" font-weight="500" fill="#555">Total Job Postings on HireScope by Occupational Sector</text>
      <text x="177" y="36" text-anchor="middle" font-size="9" fill="#666">% change in job postings since Feb 1, 2020, seasonally</text>
      <text x="177" y="50" text-anchor="middle" font-size="9" fill="#666">adjusted, to Oct 22, 2021</text>
      <g stroke="var(--grid)" stroke-width="0.7">
        <line x1="40" y1="60" x2="340" y2="60"/><line x1="40" y1="76" x2="340" y2="76"/>
        <line x1="40" y1="92" x2="340" y2="92"/><line x1="40" y1="108" x2="340" y2="108"/>
        <line x1="40" y1="124" x2="340" y2="124"/><line x1="40" y1="140" x2="340" y2="140"/>
        <line x1="40" y1="156" x2="340" y2="156"/><line x1="40" y1="172" x2="340" y2="172"/>
        <line x1="40" y1="188" x2="340" y2="188"/>
      </g>
      <g font-size="6.5" fill="#777" text-anchor="end">
        <text x="35" y="62">100%</text><text x="35" y="78">80%</text><text x="35" y="94">60%</text>
        <text x="35" y="110">40%</text><text x="35" y="126">20%</text><text x="35" y="142">0%</text>
        <text x="35" y="158">-20%</text><text x="35" y="174">-40%</text><text x="35" y="190">-60%</text>
      </g>
      <g font-size="6" fill="#777">
        <text transform="translate(46,204) rotate(-45)" text-anchor="end">Mar '20</text>
        <text transform="translate(74,204) rotate(-45)" text-anchor="end">May '20</text>
        <text transform="translate(102,204) rotate(-45)" text-anchor="end">Jul '20</text>
        <text transform="translate(130,204) rotate(-45)" text-anchor="end">Sep '20</text>
        <text transform="translate(158,204) rotate(-45)" text-anchor="end">Nov '20</text>
        <text transform="translate(186,204) rotate(-45)" text-anchor="end">Jan '21</text>
        <text transform="translate(214,204) rotate(-45)" text-anchor="end">Mar '21</text>
        <text transform="translate(242,204) rotate(-45)" text-anchor="end">May '21</text>
        <text transform="translate(270,204) rotate(-45)" text-anchor="end">Jul '21</text>
        <text transform="translate(298,204) rotate(-45)" text-anchor="end">Aug '21</text>
        <text transform="translate(326,204) rotate(-45)" text-anchor="end">Oct '21</text>
      </g>
      <g fill="none" stroke-width="1.3">
        <polyline stroke="var(--pink)" points="40,140 56,141 66,155 76,154 90,146 104,134 120,128 140,126 160,122 180,118 200,110 220,100 240,90 260,80 280,74 296,77 310,70 325,65 340,62"/>
        <polyline stroke="var(--green)" points="40,140 56,142 66,160 76,158 90,152 104,142 120,138 140,136 160,132 180,130 200,124 220,114 240,104 260,94 280,88 296,88 310,82 325,77 340,74"/>
        <polyline stroke="var(--orange)" points="40,140 56,142 66,164 76,166 90,160 104,152 120,148 140,146 160,144 180,142 200,138 220,130 240,122 260,114 280,110 296,109 310,106 325,101 340,98"/>
        <polyline stroke="var(--blue)" points="40,140 56,143 66,170 76,172 90,168 104,162 120,160 140,158 160,158 180,160 200,156 220,148 240,140 260,134 280,132 296,129 310,127 325,123 340,120"/>
      </g>
      <line x1="296" y1="60" x2="296" y2="188" stroke="#555" stroke-width="0.8"/>
      <circle cx="296" cy="77" r="2.5" fill="var(--pink)"/><circle cx="296" cy="88" r="2.5" fill="var(--green)"/>
      <circle cx="296" cy="109" r="2.5" fill="var(--orange)"/><circle cx="296" cy="129" r="2.5" fill="var(--blue)"/>
      <rect x="218" y="95" width="76" height="50" rx="3" fill="#e8f0fb" stroke="#9bb5d8" stroke-width="0.6"/>
      <text x="222" y="104" font-size="6.5" font-weight="700" fill="#333">Aug 27, 2021</text>
      <g font-size="6" fill="#333">
        <rect x="222" y="108" width="6" height="6" fill="var(--pink)"/><text x="231" y="113">Loading &amp; St... (78.4%)</text>
        <rect x="222" y="117" width="6" height="6" fill="var(--green)"/><text x="231" y="122">Logistic Sup... (65.7%)</text>
        <rect x="222" y="126" width="6" height="6" fill="var(--orange)"/><text x="231" y="131">Retail (39.2%)</text>
        <rect x="222" y="135" width="6" height="6" fill="var(--blue)"/><text x="231" y="140">Hospitality ... (14.3%)</text>
      </g>
    </svg>
  </div>

  <p class="postings-note">Job postings on HireScope are a real-time measure of labor market activity. On August 27, 2021, they were 39.4% above February 1, 2020, the pre-pandemic baseline, after adjusting for seasonal variation. Postings were up 1.7 percentage points in the past week and 4.2 points over the past four weeks.</p>

  <div class="card card-incentives">
    <svg width="374" height="240" viewBox="0 0 394 240" preserveAspectRatio="none" font-family="Roboto, Arial, sans-serif">
      <text x="197" y="30" text-anchor="middle" font-size="13" font-weight="700" fill="#222">More postings are advertising hiring incentives</text>
      <text x="197" y="44" text-anchor="middle" font-size="9" fill="#555">Share of job postings that advertise hiring incentives through July 16, 2021</text>
      <g stroke="var(--grid)" stroke-width="0.7">
        <line x1="48" y1="60" x2="370" y2="60"/><line x1="48" y1="92" x2="370" y2="92"/>
        <line x1="48" y1="124" x2="370" y2="124"/><line x1="48" y1="156" x2="370" y2="156"/>
        <line x1="48" y1="188" x2="370" y2="188"/>
      </g>
      <line x1="48" y1="220" x2="370" y2="220" stroke="#999" stroke-width="0.8"/>
      <g font-size="7" fill="#555" text-anchor="end">
        <text x="42" y="62">5%</text><text x="42" y="94">4%</text><text x="42" y="126">3%</text>
        <text x="42" y="158">2%</text><text x="42" y="190">1%</text><text x="42" y="222">0%</text>
      </g>
      <g font-size="7.5" fill="#333" font-weight="500" text-anchor="middle">
        <text x="58" y="233">Jul 2020</text><text x="138" y="233">Oct 2020</text><text x="214" y="233">Jan 2021</text>
        <text x="290" y="233">Apr 2021</text><text x="362" y="233">Jul 2021</text>
      </g>
      <polyline fill="none" stroke="#2a5aa6" stroke-width="1.6" points="50,162 62,160 72,159 82,155 92,154 104,153 116,152 126,150 136,147 146,144 152,142 160,146 168,146 178,145 190,145 200,144 214,143 226,141 240,140 254,138 266,134 278,128 290,121 302,114 314,106 324,100 334,94 344,87 354,85 362,82"/>
    </svg>
  </div>
</div>
</body>
</html>
```